Movie poster for drama/thriller feature

We need a movie poster for an edgy microbudget, drama/thriller feature called Stumbling My Road Past Dawn and is about a “night in the life” of an escort and her driver after she discovers that her mother, who was caring for her daughter, has died. She has just one night to raise the money to cover the arrears on her mother’s mortgage and return to collect her daughter before her very religious aunt calls Children’s Aid. On top of that she has to enlist the help of her new driver who is also very religious and hates her because she’s a “whore”. He is only doing this job because, as a Cuban refugee, he has had to take a job with his uncle, who is head of security at the agency, in order to pay him back what it cost to bring him to Canada. So, at the core of the story is this relationship between two people who hate each other but are stuck together in a car for an entire night. The third character is the uncle - head of security - who becomes increasingly "dark" and violent as the night goes on as he feels he is losing the loyalty of his nephew to a sex worker who is ripping off his boss.

So, that's the backdrop to the story.

Now, we want the poster to reflect that this is a scrappy, edgy little film, a bit controversial (just the title alone, obviously). Some of our inspiration for the poster are the kind of minimalist designs from French New Wave films (examples uploaded). The title itself can either be written out in toto or you could put the acronym in bold letters - SMRPD - with their meaning smaller below it. You can play with it, anyway, to come up with some cool. I've also included stills from the film of the three main characters - Marisol, the lead/star, Tomas (her driver) and Ignacio, the antaonist/uncle. You can crop these to make them work. I just left them full size so that you'd have more options.

If you have questions, don't hesitate to ask.

best
Derek

Target Market(s)

indie film goers, younger, city-based, hipster demographic

Industry/Entity Type

Film Production

Font styles to use
Sans Serif

Colors

Designer to choose colors to be used in the design.

Requirements
Must have
• A great look, the title, and some credits:
• tagline: one night can change your whole world
• A film by Bridget Oldcastle & Derek Fenwold
• With
• Ingrid Tolmachova
• Esteban Morales-Quiroga
• Raul Caceres Villalobos
• Cinematography
• Nate Corbell
• Produced by:
• Crooked Lantern Productions
• Pinecrest Studios
• and a credit block with:
• Bridget Oldcastle ... co-producer
• Ingrid Tolmachova ... co-producer
• Esteban Morales-Quiroga ... co-producer
• Gavin Trout ... co-producer
• Derek Fenwold ... co-producer
• Editing by
• Dana McGivney
• Production Design by
• Tiago Mendes Rocha
• Wendy Calder ... key makeup artist
• Priscilla Novak ... makeup artist Production Management
• Tessa Kimball ... production manager Second Unit Director or Assistant Director
• Tessa Kimball ... first assistant director Sound Department
• Ben Yardley ... sound editor
• Kevin Santoso ... sound recordist Stunts
• Raul Caceres Villalobos ... action coordinator
• Carl Pembry ... still photographer
• Fiona Beckett ... swing
• Monica Thorne ... still photographer
• Giulia Marchetti ... swing Costume and Wardrobe Department
• Nora Fairclough ... wardrobe
• Petra Holub ... wardrobe supervisor Transportation Department
• Rosalind Tapley ... craft service
• Maya Finch ... script supervisor
• Paolo Reyes ... production assistant
• Lucia Navarro ... craft service

```html
<!DOCTYPE html>
<html lang="en">
<head>
<meta charset="utf-8">
<title>Stumbling My Road Past Dawn — Poster</title>
<link rel="stylesheet" href="https://fonts.googleapis.com/css2?family=Anton&family=Oswald:wght@200;300;400&display=swap">
<style>
  :root {
    --backdrop: #e4e4e2;
    --paper: #ffffff;
    --ink: #111111;
    --name-green: #2f6b43;
    --name-pink: #c22a82;
    --name-red: #6e1e1e;
    --photo-dark: #1c1c1c;
    --photo-mid: #6a6a6a;
    --photo-light: #b5b5b5;
  }
  html, body {
    margin: 0;
    padding: 0;
    width: 1038px;
    height: 1200px;
    overflow: hidden;
    background: var(--backdrop);
  }
  .poster {
    position: absolute;
    left: 94px;
    top: 0;
    width: 850px;
    height: 1200px;
    background: var(--paper);
  }
  .poster svg { display: block; }
  .director-line { font-family: 'Oswald', sans-serif; font-weight: 400; font-size: 27px; fill: var(--ink); }
  .cast-name { font-family: 'Oswald', sans-serif; font-weight: 400; font-size: 20px; letter-spacing: 1.5px; }
  .cast-name--lead { fill: var(--name-pink); }
  .cast-name--driver { fill: var(--name-red); }
  .cast-name--uncle { fill: var(--name-green); }
  .title-word { font-family: 'Anton', sans-serif; fill: var(--ink); }
  .tagline { font-family: 'Oswald', sans-serif; font-weight: 200; fill: var(--ink); }
  .credit-label { font-family: 'Oswald', sans-serif; font-weight: 300; font-size: 11px; fill: var(--ink); }
  .credit-name { font-family: 'Oswald', sans-serif; font-weight: 300; font-size: 15px; fill: var(--ink); }
  .billing { font-family: 'Oswald', sans-serif; font-weight: 300; font-size: 11px; fill: var(--ink); }
  .billing .role { font-size: 5px; }
</style>
</head>
<body>
<main class="poster">
  <svg width="850" height="1200" viewBox="0 0 850 1200" xmlns="http://www.w3.org/2000/svg">
    <defs>
      <linearGradient id="still-uncle" x1="0" y1="0" x2="0" y2="1">
        <stop offset="0" stop-color="var(--photo-light)"/>
        <stop offset="1" stop-color="var(--photo-dark)"/>
      </linearGradient>
      <linearGradient id="still-lead" x1="0" y1="0" x2="1" y2="0">
        <stop offset="0" stop-color="var(--photo-dark)"/>
        <stop offset="0.5" stop-color="var(--photo-mid)"/>
        <stop offset="1" stop-color="var(--photo-dark)"/>
      </linearGradient>
      <linearGradient id="still-driver" x1="0" y1="0" x2="1" y2="1">
        <stop offset="0" stop-color="var(--photo-dark)"/>
        <stop offset="1" stop-color="var(--photo-mid)"/>
      </linearGradient>
    </defs>

    <text class="director-line" x="425" y="50" text-anchor="middle" textLength="611" lengthAdjust="spacing">A FILM BY BRIDGET OLDCASTLE &amp; DEREK FENWOLD</text>

    <text class="cast-name cast-name--uncle" x="425" y="96" text-anchor="middle" textLength="228" lengthAdjust="spacing">RAUL CACERES VILLALOBOS</text>

    <rect class="still still--uncle" x="305" y="113" width="238" height="236" fill="url(#still-uncle)" role="img" aria-label="Black and white still of Ignacio, the uncle, in a flat cap and dark jacket"/>
    <rect class="still still--lead" x="54" y="364" width="238" height="236" fill="url(#still-lead)" role="img" aria-label="Black and white still of Marisol in the back seat of a car at night"/>
    <rect class="still still--driver" x="556" y="364" width="238" height="236" fill="url(#still-driver)" role="img" aria-label="Black and white still of Tomas driving, a cross hanging from the mirror"/>

    <text class="cast-name cast-name--lead" x="268" y="631" text-anchor="end" textLength="210" lengthAdjust="spacing">INGRID TOLMACHOVA</text>
    <text class="cast-name cast-name--driver" x="794" y="631" text-anchor="end" textLength="236" lengthAdjust="spacing">ESTEBAN MORALES-QUIROGA</text>

    <g class="title">
      <text class="title-word" x="305" y="459" font-size="110" textLength="238" lengthAdjust="spacingAndGlyphs">STUMBLING</text>
      <text class="title-word" x="305" y="571" font-size="116" textLength="238" lengthAdjust="spacingAndGlyphs">MY ROAD</text>
      <text class="title-word" x="305" y="736" font-size="179" textLength="238" lengthAdjust="spacingAndGlyphs">PAST</text>
      <text class="title-word" x="305" y="892" font-size="171" textLength="238" lengthAdjust="spacingAndGlyphs">DAWN</text>
    </g>

    <g class="tagline-block">
      <text class="tagline" x="305" y="958" font-size="64" textLength="238" lengthAdjust="spacingAndGlyphs">ONE NIGHT CAN</text>
      <text class="tagline" x="305" y="1029" font-size="73" textLength="238" lengthAdjust="spacingAndGlyphs">CHANGE YOUR</text>
      <text class="tagline" x="305" y="1090" font-size="69" textLength="238" lengthAdjust="spacingAndGlyphs">WHOLE WORLD</text>
    </g>

    <g class="credit credit--camera">
      <text class="credit-label" x="54" y="1040">CINEMATOGRAPHY</text>
      <text class="credit-name" x="54" y="1060">NATE</text>
      <text class="credit-name" x="54" y="1080">CORBELL</text>
    </g>
    <g class="credit credit--producers">
      <text class="credit-label" x="795" y="1040" text-anchor="end">PRODUCED BY</text>
      <text class="credit-name" x="795" y="1060" text-anchor="end">CROOKED LANTERN PRODUCTIONS</text>
      <text class="credit-name" x="795" y="1080" text-anchor="end">PINECREST STUDIOS</text>
    </g>

    <g class="billing">
      <text x="425" y="1121" text-anchor="middle" textLength="741" lengthAdjust="spacingAndGlyphs"><tspan class="role">CO-PRODUCERS </tspan>BRIDGET OLDCASTLE, INGRID TOLMACHOVA, ESTEBAN MORALES-QUIROGA, GAVIN TROUT, DEREK FENWOLD. <tspan class="role">EDITING BY </tspan>DANA McGIVNEY. <tspan class="role">PRODUCTION DESIGN BY </tspan>TIAGO MENDES ROCHA. <tspan class="role">KEY MAKEUP ARTIST </tspan>WENDY CALDER.</text>
      <text x="425" y="1138" text-anchor="middle" textLength="741" lengthAdjust="spacingAndGlyphs"><tspan class="role">MAKEUP ARTIST PRODUCTION MANAGEMENT </tspan>PRISCILLA NOVAK. <tspan class="role">PRODUCTION MANAGER SECOND UNIT DIRECTOR OR ASSISTANT DIRECTOR </tspan>TESSA KIMBALL. <tspan class="role">FIRST ASSISTANT DIRECTOR SOUND DEPARTMENT </tspan>TESSA KIMBALL. <tspan class="role">SOUND EDITOR </tspan>BEN YARDLEY. <tspan class="role">SOUND RECORDIST STUNTS </tspan>KEVIN SANTOSO.</text>
      <text x="425" y="1155" text-anchor="middle" textLength="741" lengthAdjust="spacingAndGlyphs"><tspan class="role">ACTION COORDINATOR </tspan>RAUL CACERES VILLALOBOS. <tspan class="role">STILL PHOTOGRAPHERS </tspan>CARL PEMBRY, MONICA THORNE. <tspan class="role">SWING </tspan>FIONA BECKETT. <tspan class="role">SWING COSTUME AND WARDROBE DEPARTMENT </tspan>GIULIA MARCHETTI. <tspan class="role">WARDROBE </tspan>NORA FAIRCLOUGH. <tspan class="role">WARDROBE SUPERVISOR</tspan></text>
      <text x="425" y="1172" text-anchor="middle" textLength="536" lengthAdjust="spacingAndGlyphs"><tspan class="role">TRANSPORTATION DEPARTMENT </tspan>PETRA HOLUB. <tspan class="role">CRAFT SERVICE </tspan>ROSALIND TAPLEY. <tspan class="role">SCRIPT SUPERVISOR </tspan>MAYA FINCH. <tspan class="role">PRODUCTION ASSISTANT </tspan>PAOLO REYES. <tspan class="role">CRAFT SERVICE </tspan>LUCIA NAVARRO</text>
    </g>
  </svg>
</main>
</body>
</html>
```